Body therapist needs a business card

I need a card for my business which is teaching trainings in body therapy, the company is called Wexcombe Educational Group. I teach to massage therapists around Australia, South East Asia and the USA. I am attaching my logo which will guide you as to what colours I would like to have you consider. Please consult my website to find out more about what I do. www.corvantela.com.au

My name is Daniel Wexcombe. My phone number is (03) 9417 2608 or 0461753208. email is info@corvantela.com.au

```html
<!DOCTYPE html>
<html lang="en">
<head>
<meta charset="utf-8">
<title>Wexcombe Educational Group – Business Card</title>
<link href="https://fonts.googleapis.com/css2?family=Lato:wght@400;700&display=swap" rel="stylesheet">
<style>
  :root {
    --backdrop: #1c1c1e;
    --brown: #8f4f15;
    --brown-text: #8a4a12;
    --lime: #c9d80e;
    --red: #b8131a;
    --paper: #ffffff;
    --ink: #3a3a3a;
    --front-url: #e9cfb4;
    --divider: #e2e2e2;
  }
  * { margin: 0; padding: 0; box-sizing: border-box; }
  html, body {
    width: 1200px;
    height: 900px;
    overflow: hidden;
    background: var(--backdrop);
    font-family: "Lato", sans-serif;
  }
  .stage {
    position: relative;
    width: 1200px;
    height: 900px;
  }
  .card {
    position: absolute;
    left: 320px;
    width: 560px;
    height: 320px;
    overflow: hidden;
  }
  /* Front side */
  .card--front {
    top: 100px;
    background: var(--brown);
  }
  .front-mark {
    position: absolute;
    top: 110px;
    left: 0;
    width: 100%;
    display: flex;
    flex-direction: column;
    align-items: center;
    gap: 14px;
  }
  .front-mark__dot {
    width: 46px;
    height: 46px;
    border-radius: 50%;
    background: var(--lime);
  }
  .front-mark__name {
    color: var(--paper);
    font-weight: 400;
    font-size: 22px;
    letter-spacing: 0.5px;
  }
  .front-url {
    position: absolute;
    right: 150px;
    bottom: 34px;
    color: var(--front-url);
    font-size: 13px;
    letter-spacing: 0.6px;
  }
  /* Back side */
  .card--back {
    top: 470px;
    background: var(--paper);
  }
  .brand {
    position: absolute;
    left: 34px;
    top: 130px;
    display: flex;
    align-items: center;
    gap: 12px;
  }
  .brand__dot {
    width: 34px;
    height: 34px;
    border-radius: 50%;
    background: var(--lime);
    flex: none;
  }
  .brand__name {
    color: var(--brown-text);
    font-weight: 400;
    font-size: 20px;
    line-height: 1.15;
    width: 200px;
  }
  .divider {
    position: absolute;
    left: 300px;
    top: 20px;
    width: 1px;
    height: 280px;
    background: linear-gradient(to bottom, transparent, var(--divider) 30%, var(--divider) 70%, transparent);
  }
  .contact {
    position: absolute;
    left: 324px;
    top: 62px;
    color: var(--ink);
    font-size: 14px;
    line-height: 1.35;
  }
  .contact__name {
    color: var(--brown-text);
    font-weight: 700;
    font-size: 18px;
    margin-bottom: 8px;
  }
  .contact__list { list-style: none; }
  .contact__item {
    display: flex;
    align-items: center;
    gap: 6px;
  }
  .contact__icon {
    width: 13px;
    height: 13px;
    flex: none;
    fill: var(--brown-text);
  }
  .contact__address {
    margin-top: 14px;
    font-style: normal;
    font-size: 14px;
  }
</style>
</head>
<body>
<main class="stage">
  <section class="card card--front" aria-label="Business card, front">
    <div class="front-mark">
      <span class="front-mark__dot"></span>
      <span class="front-mark__name">Wexcombe Educational Group</span>
    </div>
    <p class="front-url">www.corvantela.com.au</p>
  </section>

  <section class="card card--back" aria-label="Business card, back">
    <div class="brand">
      <span class="brand__dot"></span>
      <span class="brand__name">Wexcombe Educational Group</span>
    </div>
    <div class="divider"></div>
    <div class="contact">
      <h1 class="contact__name">Daniel Wexcombe</h1>
      <ul class="contact__list">
        <li class="contact__item">
          <svg class="contact__icon" viewBox="0 0 16 16" aria-hidden="true"><path d="M3.5 1.5l2.5 0 1 3.5-1.6 1.2a8.5 8.5 0 0 0 4.4 4.4L11 9l3.5 1v2.5c0 1-1 2-2 2A11 11 0 0 1 1.5 3.5c0-1 1-2 2-2z"/></svg>
          +61 (03) 9417 2608
        </li>
        <li class="contact__item">
          <svg class="contact__icon" viewBox="0 0 16 16" aria-hidden="true"><path d="M1 3h14v10H1z M2 4.2v.4l6 4.2 6-4.2v-.4z" fill-rule="evenodd"/></svg>
          info@corvantela.com.au
        </li>
        <li class="contact__item">
          <svg class="contact__icon" viewBox="0 0 16 16" aria-hidden="true"><circle cx="8" cy="8" r="7"/></svg>
          www.corvantela.com.au
        </li>
      </ul>
      <address class="contact__address">P.O. Box 2274, Ashvale East<br>Victoria, 3187 Australia</address>
    </div>
  </section>
</main>
</body>
</html>
```